Schlichtes Design für Malerbetrieb
Zielgruppe
Wir sind ein mittelgroßer Malerbetrieb in München mit umfangreichem Leistungsspektrum.
Unsere Hauptleistungen sind: Fassadenrenovierung, Altbausanierung, Betoninstandsetzung, Balkonabdichtung (kein Neubau!).
Unsere Zielgruppen sind: Hausverwaltungen, Firmen und Privatpersonen.
Unsere Kunden schätzen: Konstruktive Organisation und Planung im Vorfeld, Zuverlässigkeit, saubere Arbeitsweise, dauerhafte Balkonabdichtungen.
Aufgabenstellung
Wir möchten eine langlebige, stilvolle, minimalistische Homepage.
Wir möchten von der bestehenden Homepage nur die Schriftart für unseren Firmennamen (Century Gothic) und wenn möglich (nicht zwingend), irgendwo das florale Muster einbauen. Corporate-Design haben wir nicht.
Farbtöne: Firmennamen Orange (hellorange bis erdiges Orange möglich, da sind wir nicht fixiert) , einen dunklen Hintergrundfarbton (Petrol-Blaugrau ?) mit gelbem (neon bis senfgelb) Akzent (Linien), Blumenmuster weiß, grau.
Dies sind nur unsere Ideen. Wir sind aber auch absolut offen für eure Profi-Ideen.
Wir möchten uns von den unzähligen langweiligen 'Pinselseiten mit veralteten Bilder' unserer Kollegen interessant und mit Stil abheben.
Eher nach dem Motto 'weniger ist mehr'.
Einen positiven, sympathischen Eindruck geben und unsere Leistungen in den Vordergrund bringen.
Da wir viele Stammkunden haben, betreiben wir kein Social-Media und möchten dies vorerst auch nicht tun.
Die Seite wird in den nächsten Jahren nicht verändert, höchstens die Bilder aktualisiert.
Die Texte haben wir alle selbst entworfen und möchten wir so übernehmen.
Die Galerien sollen unkompliziert anzuschauen sein.
Uns gefällt die Struktur und Schlichtheit von https://vormtakel.nl/ oder Tessuri.de gut und wir mögen Vintage-Grafiken gerne.
Einerseits darf die Seite geradlinig, andererseits aber auch rund und floral wirken.

```html
<!DOCTYPE html>
<html lang="de">
<head>
<meta charset="utf-8">
<title>Feldner – Malerbetrieb</title>
<link href="https://fonts.googleapis.com/css2?family=Jost:wght@400;500;700&family=Questrial&display=swap" rel="stylesheet">
<style>
  :root {
    --orange: #e06a0c;
    --ink: #1e242c;
    --beige: #ece6df;
    --plaster: #f4f2ec;
    --white: #ffffff;
    --rule: #8a5a36;
  }
  * { box-sizing: border-box; margin: 0; padding: 0; }
  html, body { width: 1200px; height: 1115px; overflow: hidden; background: var(--white); }
  .page { position: relative; width: 1200px; height: 1115px; font-family: "Questrial", sans-serif; color: var(--ink); }

  .hero-photo { position: absolute; left: 0; top: 0; width: 754px; height: 750px;
    background: radial-gradient(ellipse at 40% 30%, #fdfdf9 0%, #f1efe8 45%, #d9d6cd 80%, #b9b5ab 100%); }
  .hero-beige { position: absolute; left: 754px; top: 0; width: 446px; height: 416px; background: var(--beige); }
  .hero-orange { position: absolute; left: 754px; top: 416px; width: 446px; height: 334px; background: var(--orange); }
  .hero-art { position: absolute; left: 943px; top: 193px; width: 182px; height: 276px;
    background: linear-gradient(135deg, #8fb3a4 0%, #c8542a 40%, #d8622a 60%, #4a4f60 100%); }

  .brand { position: absolute; left: 75px; top: 62px; font-family: "Jost", sans-serif; font-weight: 500;
    font-size: 23px; color: var(--orange); letter-spacing: 0.5px; }
  .main-nav { position: absolute; top: 69px; left: 598px; display: flex; gap: 0; }
  .main-nav a { position: absolute; white-space: nowrap; font-size: 15px; color: var(--ink); text-decoration: none; }
  .main-nav a.active { color: var(--orange); font-weight: 700; font-family: "Jost", sans-serif; }

  .service-list { position: absolute; right: 280px; top: 244px; text-align: right; list-style: none;
    font-family: "Jost", sans-serif; font-weight: 500; font-size: 14.5px; letter-spacing: 0.3px; }
  .service-list li { height: 33.7px; }

  .wordmark { position: absolute; left: 200px; top: 540px; }

  .btn-about { position: absolute; left: 998px; top: 647px; width: 127px; height: 35px;
    border: 1px solid var(--ink); font-family: "Jost", sans-serif; font-size: 12.5px; letter-spacing: 2px;
    display: flex; align-items: center; justify-content: center; color: var(--ink); text-decoration: none; }

  .services { position: absolute; left: 0; top: 750px; width: 1200px; height: 223px; }
  .services-title { position: absolute; left: 0; top: 0; width: 308px; height: 223px;
    background: linear-gradient(180deg, #c9733a 0%, #d06a2a 60%, #c9662a 100%); }
  .services-title h2 { position: absolute; left: 74px; top: 136px; font-weight: 400; font-size: 26px; color: var(--white); letter-spacing: 0.5px; }
  .service-tile { position: absolute; top: 0; height: 223px; }
  .service-tile .frame { position: absolute; left: 25px; top: 25px; width: 173px; height: 172px;
    border: 2px solid var(--white); text-align: center; color: var(--white); }
  .service-tile .frame span { display: block; margin-top: 40px; font-size: 15px; letter-spacing: 0.4px; }
  .service-tile svg { position: absolute; left: 66px; top: 86px; }
  .tile-1 { left: 308px; width: 222px; background: linear-gradient(160deg, #2a3040 0%, #141a2a 100%); }
  .tile-2 { left: 530px; width: 224px; background: linear-gradient(180deg, #2c3647 0%, #1e2634 100%); }
  .tile-3 { left: 754px; width: 223px; background: linear-gradient(170deg, #4a5060 0%, #262a35 60%, #1c2029 100%); }
  .tile-4 { left: 977px; width: 223px; background: linear-gradient(180deg, #262b2c 0%, #161a1c 100%); }

  .site-footer { position: absolute; left: 0; top: 973px; width: 1200px; height: 142px; background: var(--ink); }
  .site-footer hr { position: absolute; left: 75px; top: 49px; width: 1051px; border: 0; border-top: 1px solid var(--rule); }
  .copyright { position: absolute; left: 75px; top: 70px; font-family: "Jost", sans-serif; font-size: 12px; color: var(--white); }
  .legal { position: absolute; right: 74px; top: 70px; display: flex; gap: 18px; align-items: center;
    font-family: "Jost", sans-serif; font-size: 12px; }
  .legal a { color: var(--white); text-decoration: none; }
  .legal .dot { width: 14px; height: 14px; border-radius: 50%; background: var(--white); }
</style>
</head>
<body>
<div class="page">
  <div class="hero-photo" role="img" aria-label="Nahaufnahme einer weißen Stuckverzierung"></div>
  <div class="hero-beige" role="img" aria-label="Heller Hintergrund mit floralem Muster"></div>
  <div class="hero-orange"></div>
  <div class="hero-art" role="img" aria-label="Orangefarbenes florales Ornament auf blaugrünem Grund"></div>

  <div class="brand">feldner</div>

  <nav class="main-nav">
    <a class="active" href="#" style="left:0">Home</a>
    <a href="#" style="left:72px">Leistungen</a>
    <a href="#" style="left:178px">Portrait</a>
    <a href="#" style="left:258px">Referenzen</a>
    <a href="#" style="left:366px">Ausbildung</a>
    <a href="#" style="left:475px">Kontakt</a>
  </nav>

  <ul class="service-list">
    <li>Malerarbeiten</li>
    <li>Betoninstandsetzung</li>
    <li>Höchstdruckstrahlen</li>
    <li>Balkonabdichtung</li>
  </ul>

  <svg class="wordmark" width="760" height="160" viewBox="0 0 760 160" aria-label="feldner">
    <text x="2" y="142" font-family="Jost, sans-serif" font-weight="700" font-size="190" fill="#1e242c"
      textLength="750" lengthAdjust="spacingAndGlyphs">feldner</text>
  </svg>

  <a class="btn-about" href="#">Über uns</a>

  <section class="services">
    <div class="services-title" role="img" aria-label="Altbaufassade in Orange getönt"><h2>Leistungen</h2></div>

    <div class="service-tile tile-1" role="img" aria-label="Gestrichene Hauswand bei Nacht">
      <div class="frame"><span>Malerarbeiten</span>
        <svg width="40" height="40" viewBox="0 0 40 40"><circle cx="20" cy="20" r="18.5" fill="none" stroke="#fff" stroke-width="1.5"/>
          <rect x="12" y="12" width="15" height="5" rx="1" fill="#fff"/><path d="M27 14.5h2v5h-9v3" fill="none" stroke="#fff" stroke-width="1.5"/><rect x="18.5" y="22" width="3" height="8" fill="#fff"/></svg>
      </div>
    </div>
    <div class="service-tile tile-2" role="img" aria-label="Betonfassade eines Parkhauses">
      <div class="frame"><span>Betoninstandsetzung</span>
        <svg width="40" height="40" viewBox="0 0 40 40"><circle cx="20" cy="20" r="18.5" fill="none" stroke="#fff" stroke-width="1.5"/>
          <path d="M11 27l8-5 3 4z" fill="#fff"/><path d="M20 23l8-10" stroke="#fff" stroke-width="2.5" stroke-linecap="round"/></svg>
      </div>
    </div>
    <div class="service-tile tile-3" role="img" aria-label="Wasserstrahl auf Asphalt">
      <div class="frame"><span>Höchstdruckstrahlen</span>
        <svg width="40" height="40" viewBox="0 0 40 40"><circle cx="20" cy="20" r="18.5" fill="none" stroke="#fff" stroke-width="1.5"/>
          <path d="M12 13h15v4H17l-2 9h-3l2-9h-2z" fill="#fff"/><path d="M28 15h3" stroke="#fff" stroke-width="1.5"/></svg>
      </div>
    </div>
    <div class="service-tile tile-4" role="img" aria-label="Balkon an einer Hausfassade">
      <div class="frame"><span>Balkonabdichtung</span>
        <svg width="40" height="40" viewBox="0 0 40 40"><circle cx="20" cy="20" r="18.5" fill="none" stroke="#fff" stroke-width="1.5"/>
          <rect x="15" y="10" width="10" height="11" fill="none" stroke="#fff" stroke-width="1.3"/><path d="M20 10v11M15 15.5h10" stroke="#fff" stroke-width="1"/>
          <path d="M11 22h18M12 22v6M15 22v6M18 22v6M21 22v6M24 22v6M27 22v6M11 28h18" stroke="#fff" stroke-width="1.2"/></svg>
      </div>
    </div>
  </section>

  <footer class="site-footer">
    <hr>
    <p class="copyright">© Copyright Feldner GmbH 2009 - 2020, Alle Rechte vorbehalten.</p>
    <nav class="legal">
      <a href="#">Impressum</a>
      <a href="#">Rechtliche Hinweisse</a>
      <a href="#">Datenschutzerklärung</a>
      <span class="dot"></span>
    </nav>
  </footer>
</div>
</body>
</html>
```